YARD FRONTS "N" MORE

catyering to driveway/patio floor construction and remodeling. Concrete, concrete pavers, asphalt, Landscaping, irrigation, pergolas and pools.

Target Market(s)

the home owner that wants to enhance their home

Industry/Entity Type

construction

Contact Information for Business Card

presidet: tomas bellweather email: yardfrontsnmore@example.come office/cell: 555 214 8830

Font styles to use
Sans Serif

Requirements
Must have
• logo should pop out
Nice to have
• the logo should demonstrate that we do exteriors only

```html
<!DOCTYPE html>
<html lang="en">
<head>
<meta charset="utf-8">
<title>Yard Fronts "N" More – Business Card</title>
<link rel="stylesheet" href="https://fonts.googleapis.com/css2?family=Poppins:wght@400;500;700&family=Montserrat:wght@500&display=swap">
<style>
  :root {
    --page-bg: #cbcccc;
    --front-dark: #0c2b42;
    --front-mid: #123a55;
    --back-dark: #0d5077;
    --back-mid: #14608b;
    --accent: #2e93cf;
    --white: #ffffff;
    --pill: #1a5a82;
  }
  * { box-sizing: border-box; margin: 0; padding: 0; }
  html, body { width: 750px; height: 1200px; overflow: hidden; }
  body {
    background: var(--page-bg);
    font-family: "Poppins", Arial, sans-serif;
    color: var(--white);
    position: relative;
  }
  .card {
    position: absolute;
    left: 75px;
    width: 600px;
    height: 342px;
    box-shadow: 4px 6px 10px rgba(0,0,0,0.28);
    overflow: hidden;
  }
  .card-front {
    top: 225px;
    background: radial-gradient(ellipse at 40% 40%, var(--front-mid), var(--front-dark) 75%);
  }
  .card-back {
    top: 633px;
    background: radial-gradient(ellipse at 50% 45%, var(--back-mid), var(--back-dark) 80%);
  }
  .holder { position: absolute; left: 48px; top: 48px; }
  .holder-name { font-size: 30px; line-height: 1; letter-spacing: 0.2px; }
  .holder-first { font-weight: 700; }
  .holder-last { font-weight: 400; color: var(--accent); }
  .holder-title { font-size: 17px; margin-top: 6px; font-weight: 400; }

  .contact { position: absolute; left: 48px; top: 242px; display: flex; gap: 10px; }
  .contact-icons {
    width: 22px; height: 57px; border-radius: 11px; background: var(--pill);
    display: flex; flex-direction: column; justify-content: space-around; align-items: center;
    padding: 3px 0;
  }
  .contact-icons svg { width: 11px; height: 11px; }
  .contact-lines { font-size: 15.5px; line-height: 18.5px; margin-top: -1px; }

  .brand-mark {
    position: absolute; display: flex; flex-direction: column; align-items: center;
  }
  .card-front .brand-mark { right: 44px; top: 190px; }
  .card-back .brand-mark { left: 0; right: 0; top: 92px; }
  .brand-square { border: 3px solid var(--white); }
  .card-front .brand-square { width: 60px; height: 60px; }
  .card-back .brand-square { width: 72px; height: 72px; }
  .brand-name {
    font-family: "Montserrat", Arial, sans-serif; font-weight: 500;
    color: var(--white); white-space: nowrap;
  }
  .card-front .brand-name { font-size: 14px; letter-spacing: 2px; margin-top: 10px; }
  .card-back .brand-name { font-size: 19px; letter-spacing: 3px; margin-top: 24px; }

  .web {
    position: absolute; left: 0; right: 0; top: 284px; text-align: center;
    font-family: "Montserrat", Arial, sans-serif; font-weight: 500;
    font-size: 14px; letter-spacing: 4px;
  }
</style>
</head>
<body>
  <section class="card card-front">
    <div class="holder">
      <h1 class="holder-name"><span class="holder-first">TOMAS</span> <span class="holder-last">BELLWEATHER</span></h1>
      <p class="holder-title">President</p>
    </div>
    <div class="contact">
      <div class="contact-icons">
        <svg viewBox="0 0 24 24" aria-hidden="true"><path fill="#fff" d="M6.6 10.8a15 15 0 0 0 6.6 6.6l2.2-2.2c.3-.3.7-.4 1-.2 1.1.4 2.3.6 3.6.6.6 0 1 .4 1 1V20c0 .6-.4 1-1 1A17 17 0 0 1 3 4c0-.6.4-1 1-1h3.5c.6 0 1 .4 1 1 0 1.3.2 2.5.6 3.6.1.3 0 .7-.2 1z"/></svg>
        <svg viewBox="0 0 24 24" aria-hidden="true"><rect x="2" y="5" width="20" height="14" fill="#fff"/><path d="M2 5l10 8 10-8M2 19l7-7M22 19l-7-7" stroke="#1a5a82" stroke-width="1.8" fill="none"/></svg>
        <svg viewBox="0 0 24 24" aria-hidden="true"><g fill="none" stroke="#fff" stroke-width="2"><circle cx="12" cy="12" r="9"/><ellipse cx="12" cy="12" rx="4" ry="9"/><path d="M3 12h18M5 7h14M5 17h14"/></g></svg>
      </div>
      <div class="contact-lines">
        <p>555 214 8830</p>
        <p>yardfrontsnmore@example.com</p>
        <p>www.yardfrontsnmore.example</p>
      </div>
    </div>
    <div class="brand-mark">
      <div class="brand-square"></div>
      <p class="brand-name">YARD FRONTS</p>
    </div>
  </section>

  <section class="card card-back">
    <div class="brand-mark">
      <div class="brand-square"></div>
      <p class="brand-name">YARD FRONTS</p>
    </div>
    <p class="web">www.yardfrontsnmore.example</p>
  </section>
</body>
</html>
```